Corvanta Business cards template

We're looking for something modern and elegant. We are a reseller of technology (computers, datacenter, etc). Color theme would be "only" white with the incorporation of the blue that's present on our website (Corvanta.com) and logo file. We would like for the card to provide all the necessary info for the specific person (Phone#, fax#, email, name, website URL) . I'm attaching the logo file to this request. Please have it show Montreal/New York somewhere, without providing specific addresses.

Target Market(s)

All b2b

Industry/Entity Type

Business

Contact Information for Business Card

Please have the color scheme be represented by only the white and blue from our website (Corvanta.com) and logo. We would like to logo on the card, but not big and overwhelming. This card will be used as a template for anybody within the company, it should display the user's name, phone#, fax#, email, job title and website URL. Please have it show Montreal/New York somewhere, without providing our specific addresses. Really, we're looking for a clean, simple and elegant look.

Font styles to use
Serif

Requirements
Must have
• Please see card details
Nice to have
• Please see card details
Should not have
• Anything tacky or tagline.

```html
<!DOCTYPE html>
<html lang="en">
<head>
<meta charset="utf-8">
<title>Corvanta Business Card</title>
<link rel="stylesheet" href="https://fonts.googleapis.com/css2?family=Open+Sans:wght@400;600;700&display=swap">
<style>
  :root {
    --page-bg: #e4e6e9;
    --card-white: #ffffff;
    --card-back: #f1f1f2;
    --brand-blue: #1a8fd8;
    --ink: #1f1f1f;
    --divider: #9a9a9a;
    --band-grey: #505152;
    --band-text: #f2f2f2;
  }
  * { box-sizing: border-box; margin: 0; padding: 0; }
  html, body { width: 1200px; height: 960px; overflow: hidden; }
  body {
    background: var(--page-bg);
    font-family: "Open Sans", Arial, sans-serif;
    position: relative;
  }
  .card {
    position: absolute;
    left: 320px;
    width: 560px;
    height: 320px;
    box-shadow: 0 6px 18px rgba(0,0,0,0.18);
    overflow: hidden;
  }
  .card--back {
    top: 100px;
    background: var(--card-back);
    display: flex;
    align-items: center;
    justify-content: center;
  }
  .card--front {
    top: 520px;
    background: var(--card-white);
  }
  .brand-name {
    color: var(--brand-blue);
    font-weight: 600;
    font-size: 52px;
    letter-spacing: 0.5px;
    line-height: 1;
  }
  .card--front .brand-name {
    position: absolute;
    left: 50px;
    top: 128px;
    font-size: 46px;
  }
  .divider {
    position: absolute;
    left: 315px;
    top: 28px;
    width: 1px;
    height: 210px;
    background: var(--divider);
  }
  .person {
    position: absolute;
    left: 340px;
    top: 34px;
  }
  .person__name {
    color: var(--brand-blue);
    font-weight: 700;
    font-size: 26px;
    line-height: 1.1;
  }
  .person__title {
    color: var(--brand-blue);
    font-weight: 700;
    font-size: 13px;
    letter-spacing: 0.6px;
    margin-left: 8px;
  }
  .contact-list {
    position: absolute;
    left: 340px;
    top: 140px;
    list-style: none;
  }
  .contact-list li {
    display: flex;
    align-items: center;
    gap: 10px;
    font-size: 15px;
    color: var(--ink);
    height: 23px;
    white-space: nowrap;
  }
  .contact-list .icon {
    width: 16px;
    height: 16px;
    flex: none;
  }
  .rule-blue {
    position: absolute;
    left: 0; right: 0;
    top: 246px;
    height: 4px;
    background: var(--brand-blue);
  }
  .location-band {
    position: absolute;
    left: 0; right: 0;
    top: 254px;
    bottom: 0;
    background: var(--band-grey);
    color: var(--band-text);
    display: flex;
    align-items: center;
    justify-content: center;
    font-size: 15px;
    letter-spacing: 0.8px;
    text-transform: uppercase;
  }
</style>
</head>
<body>

<section class="card card--back">
  <span class="brand-name">Corvanta</span>
</section>

<section class="card card--front">
  <span class="brand-name">Corvanta</span>
  <div class="divider"></div>

  <div class="person">
    <div class="person__name">Lena Vostrik</div>
    <div class="person__title">Your Position</div>
  </div>

  <ul class="contact-list">
    <li>
      <svg class="icon" viewBox="0 0 16 16" aria-hidden="true">
        <rect width="16" height="16" fill="var(--brand-blue)"/>
        <path d="M4.5 3.5l2 2-1 1.2c.6 1.3 1.6 2.3 2.8 2.8l1.2-1 2 2-1.2 1.5C7 11.8 4.2 9 3 5.5z" fill="#fff"/>
      </svg>
      1-855-555-CORV (2678)
    </li>
    <li>
      <svg class="icon" viewBox="0 0 16 16" aria-hidden="true">
        <rect width="16" height="16" fill="var(--brand-blue)"/>
        <rect x="4" y="3" width="8" height="4" fill="#fff"/>
        <rect x="3" y="7.5" width="10" height="5" fill="#fff"/>
        <rect x="5" y="9" width="6" height="1" fill="var(--brand-blue)"/>
      </svg>
      1-855-555-(2679)
    </li>
    <li>
      <svg class="icon" viewBox="0 0 16 16" aria-hidden="true">
        <rect width="16" height="16" fill="var(--brand-blue)"/>
        <rect x="3" y="4.5" width="10" height="7" fill="#fff"/>
        <path d="M3 4.5l5 4 5-4" fill="none" stroke="var(--brand-blue)" stroke-width="1"/>
      </svg>
      info@corvanta.com
    </li>
    <li>
      <svg class="icon" viewBox="0 0 16 16" aria-hidden="true">
        <rect width="16" height="16" fill="var(--brand-blue)"/>
        <circle cx="8" cy="8" r="4.8" fill="none" stroke="#fff" stroke-width="1.2"/>
        <ellipse cx="8" cy="8" rx="2" ry="4.8" fill="none" stroke="#fff" stroke-width="1"/>
        <line x1="3.2" y1="8" x2="12.8" y2="8" stroke="#fff" stroke-width="1"/>
      </svg>
      www.corvanta.com
    </li>
  </ul>

  <div class="rule-blue"></div>
  <div class="location-band">Montreal &nbsp;|&nbsp; New York</div>
</section>

</body>
</html>
```